Anzeigengestaltung für Zahnarztpraxis
Zielgruppe
Zahnarztpraxis
Aufgabenstellung
Möchte eine moderne Stellenanzeige, ggf. einen zum Logo farblich passenden Rahmen; ggf. noch mit Bildern

```html
<!DOCTYPE html>
<html lang="de">
<head>
<meta charset="utf-8">
<title>Stellenanzeige Zahnarztpraxis Lindental</title>
<link rel="stylesheet" href="https://fonts.googleapis.com/css2?family=Crimson+Text:wght@400;700&family=Arimo&display=swap">
<style>
  :root {
    --frame-blue: #1c1ca8;
    --frame-lime: #d6f200;
    --paper: #ffffff;
    --ink: #111111;
    --brand: #1f3f73;
    --brand-accent: #8cc63f;
  }
  * { margin: 0; padding: 0; box-sizing: border-box; }
  html, body { width: 1200px; height: 852px; overflow: hidden; background: var(--paper); }
  .ad {
    position: relative;
    width: 1200px; height: 852px;
    background: var(--frame-blue);
    padding: 9px 8px 8px 9px;
    font-family: "Crimson Text", Georgia, serif;
    color: var(--ink);
  }
  .ad__band {
    width: 100%; height: 100%;
    background: var(--frame-lime);
    padding: 12px 13px 14px 12px;
  }
  .ad__sheet {
    position: relative;
    width: 100%; height: 100%;
    background: var(--paper);
  }
  .brand {
    position: absolute; left: 300px; top: 40px;
    display: flex; align-items: center; gap: 28px;
  }
  .brand__dot {
    width: 110px; height: 110px; border-radius: 50%;
    background: var(--brand-accent);
  }
  .brand__name {
    font-size: 46px; font-weight: 700; line-height: 1.05;
    color: var(--brand);
  }
  .job-titles {
    position: absolute; left: 0; right: 0; top: 200px;
    text-align: center; font-weight: 700; font-size: 25px; line-height: 41px;
  }
  .job-titles span { display: inline-block; margin-left: 26px; }
  .job-scope {
    position: absolute; left: 0; right: 0; top: 312px;
    text-align: center; font-family: "Arimo", Arial, sans-serif; font-size: 22px;
  }
  .list {
    position: absolute; top: 390px;
    font-size: 15.5px; line-height: 27.5px; list-style: none;
  }
  .list--benefits { left: 117px; }
  .list--values { left: 607px; }
  .list__head { margin-bottom: 2px; }
  .list__item::before { content: "\2713"; display: inline-block; width: 22px; font-size: 15px; }
  .contact {
    position: absolute; left: 0; right: 0; top: 638px;
    text-align: center; font-size: 19px; line-height: 29px;
  }
  .contact strong { font-weight: 700; margin-left: 8px; }
</style>
</head>
<body>
<div class="ad">
  <div class="ad__band">
    <div class="ad__sheet">
      <div class="brand">
        <div class="brand__dot"></div>
        <div class="brand__name">Zahnarztpraxis<br>Lindental</div>
      </div>

      <h1 class="job-titles">
        Zahnmedizinische Fachangestellte <span>(m/w/d)</span><br>
        Zahnmedizinische Prophylaxeassistent <span>(m/w/d)</span>
      </h1>

      <p class="job-scope">in Vollzeit gesucht</p>

      <ul class="list list--benefits">
        <li class="list__head">Deine Vorteile:</li>
        <li class="list__item">Geregelte Arbeitszeiten</li>
        <li class="list__item">Top moderne Ausstattung</li>
        <li class="list__item">Spannende Mitarbeiterevents und Spaß bei der Arbeit</li>
        <li class="list__item">Etabliertes Qualitätsmanagement und klare Strukturen</li>
        <li class="list__item">Flexible Urlaubsplanung</li>
        <li class="list__item">Überdurchschnittliches Gehalt</li>
        <li class="list__item">Kostenfreie Zahnbehandlungen inkl. Bleaching</li>
      </ul>

      <ul class="list list--values">
        <li class="list__head">Was uns wichtig ist:</li>
        <li class="list__item">Du bist aufgeschlossen und motiviert</li>
        <li class="list__item">Du bist kommunikativ und kontaktfreudig im Umgang mit Menschen</li>
        <li class="list__item">Du hast Freude an Deiner Arbeit</li>
        <li class="list__item">Dann bist <strong>DU</strong> die Verstärkung, die wir suchen!</li>
      </ul>

      <div class="contact">
        <p>Interesse?</p>
        <p>Wir freuen uns über eine schriftliche Bewerbung</p>
        <p>per Post an: <strong>Dr. Harbeck, Lindenweg 12, 73400 Lindental</strong></p>
        <p>oder per Mail an: <strong>timo-harbeck@postfach24.de</strong></p>
      </div>
    </div>
  </div>
</div>
</body>
</html>
```